Craft brewery keg badge / badge branding to be on display on keg fonts in pubs and craft beer bars

We're a small craft beer producer and are looking to have a keg badge designed to be put onto keg fonts in bars as well as being used on our bottles. Our website is www.qlbrewery.co.uk. -Please take a look at our site however we're looking for new branding! We're not looking to have the windmill on the badge! We want a bold geometric hop design in the centre of the design. The beer is a low AVB beer (2.9% ABV) and will be hopped with Cascade, Colombus and Mosaic hops and will have a fruity / juicy aroma. We're looking to have a design that we can re-use again and again by changing: colours and wording for different beers in the future.

Target Market(s)
Craft beer drinkers
Industry/Entity Type
Craft Brewery
Requirements
Must have
- Simple, elegant, repeatable core message from the badge. It need a simple, bold geometric hop design (examples uploaded) in the centre which is repeatable across many brands in the future.
- The badge needs to be circular and 82mm across to fit our tap lenses (see http://www.velmo.co.uk/branding for the flat lens). The keg badge needs to be modern and in line with other keg badges like the examples attached- though we leave the artistic flair up to you guys. Please see below the styles of keg badge we like.
- Must be in vector file format and we must get a jpeg version too.

Should not have
- Should not be overcrowded and try to be too full of information. See attached examples.

```html
<!DOCTYPE html>
<html lang="en">
<head>
<meta charset="utf-8">
<title>Keg Badges – Table Beer</title>
<link href="https://fonts.googleapis.com/css2?family=Rye&family=Oswald:wght@400;600&display=swap" rel="stylesheet">
<style>
  :root {
    --page: #eeeef0;
    --title: #2a2a2a;
    --label: #ffffff;
    --hop-light: #9bd447;
    --hop-dark: #3f8f2a;
    --aqua-light: #7fe3ff;
    --aqua-dark: #1aa9e0;
    --rose-light: #ff8fa8;
    --rose-dark: #e2305f;
    --sky-light: #8fd0ff;
    --sky-dark: #1f7fe0;
    --amber-light: #ffe680;
    --amber-dark: #f6a623;
  }
  html, body {
    margin: 0;
    padding: 0;
    width: 1200px;
    height: 1039px;
    overflow: hidden;
    background: var(--page);
  }
  .sheet {
    position: relative;
    width: 1200px;
    height: 1039px;
  }
  .sheet-title {
    position: absolute;
    left: 54px;
    top: 52px;
    margin: 0;
    font-family: "Rye", serif;
    font-weight: 400;
    font-size: 82px;
    line-height: 84px;
    letter-spacing: 2px;
    color: var(--title);
    text-shadow: 3px 3px 0 rgba(0,0,0,0.18);
  }
  .badge {
    position: absolute;
    filter: drop-shadow(0 2px 3px rgba(0,0,0,0.25));
  }
  .badge-aqua  { left: 450px; top: 30px;  width: 300px; height: 300px; }
  .badge-rose  { left: 818px; top: 28px;  width: 300px; height: 300px; }
  .badge-sky   { left: 54px;  top: 342px; width: 300px; height: 300px; }
  .badge-amber { left: 54px;  top: 700px; width: 300px; height: 300px; }
  .badge-feature { left: 533px; top: 473px; width: 460px; height: 460px; }
  .badge-name {
    font-family: "Oswald", sans-serif;
    font-weight: 600;
    font-size: 28px;
    fill: var(--label);
    letter-spacing: 0.5px;
  }
  .badge-strength {
    font-family: "Oswald", sans-serif;
    font-weight: 400;
    font-size: 22px;
    fill: var(--label);
  }
  .badge-rule { stroke: var(--label); stroke-width: 1.5; }
</style>
</head>
<body>
<main class="sheet">
  <h1 class="sheet-title">KEG<br>BADGES</h1>

  <svg width="0" height="0" style="position:absolute" aria-hidden="true">
    <defs>
      <radialGradient id="fill-aqua" cx="50%" cy="40%" r="60%">
        <stop offset="0%" stop-color="var(--aqua-light)"/>
        <stop offset="100%" stop-color="var(--aqua-dark)"/>
      </radialGradient>
      <radialGradient id="fill-rose" cx="50%" cy="40%" r="60%">
        <stop offset="0%" stop-color="var(--rose-light)"/>
        <stop offset="100%" stop-color="var(--rose-dark)"/>
      </radialGradient>
      <radialGradient id="fill-sky" cx="50%" cy="40%" r="60%">
        <stop offset="0%" stop-color="var(--sky-light)"/>
        <stop offset="100%" stop-color="var(--sky-dark)"/>
      </radialGradient>
      <radialGradient id="fill-amber" cx="50%" cy="40%" r="60%">
        <stop offset="0%" stop-color="var(--amber-light)"/>
        <stop offset="100%" stop-color="var(--amber-dark)"/>
      </radialGradient>
      <linearGradient id="fill-hop" x1="0" y1="0" x2="0" y2="1">
        <stop offset="0%" stop-color="var(--hop-light)"/>
        <stop offset="100%" stop-color="var(--hop-dark)"/>
      </linearGradient>
      <g id="badge-face">
        <ellipse cx="150" cy="106" rx="56" ry="80" fill="url(#fill-hop)" role="img" aria-label="Geometric green hop cone illustration"/>
        <text class="badge-name" x="150" y="232" text-anchor="middle">TABLE BEER</text>
        <line class="badge-rule" x1="86" y1="240" x2="214" y2="240"/>
        <text class="badge-strength" x="150" y="266" text-anchor="middle">2.9% ABV</text>
      </g>
    </defs>
  </svg>

  <svg class="badge badge-aqua" viewBox="0 0 300 300" role="img" aria-label="Table Beer keg badge, aqua water texture">
    <circle cx="150" cy="150" r="148" fill="url(#fill-aqua)" stroke="#1593c4" stroke-width="2"/>
    <use href="#badge-face"/>
  </svg>

  <svg class="badge badge-rose" viewBox="0 0 300 300" role="img" aria-label="Table Beer keg badge, pink crystal texture">
    <circle cx="150" cy="150" r="148" fill="url(#fill-rose)" stroke="#c4244f" stroke-width="2"/>
    <circle cx="150" cy="150" r="134" fill="none" stroke="#9b4fb0" stroke-width="2.5" opacity="0.7"/>
    <use href="#badge-face"/>
  </svg>

  <svg class="badge badge-sky" viewBox="0 0 300 300" role="img" aria-label="Table Beer keg badge, blue ice texture">
    <circle cx="150" cy="150" r="148" fill="url(#fill-sky)" stroke="#1a66c0" stroke-width="2"/>
    <use href="#badge-face"/>
  </svg>

  <svg class="badge badge-amber" viewBox="0 0 300 300" role="img" aria-label="Table Beer keg badge, amber watercolour texture">
    <circle cx="150" cy="150" r="148" fill="url(#fill-amber)" stroke="#e09015" stroke-width="2"/>
    <circle cx="150" cy="150" r="130" fill="none" stroke="#fff27a" stroke-width="3" opacity="0.8"/>
    <use href="#badge-face"/>
  </svg>

  <svg class="badge badge-feature" viewBox="0 0 300 300" role="img" aria-label="Table Beer keg badge, blue ice texture, feature size">
    <circle cx="150" cy="150" r="148" fill="url(#fill-sky)" stroke="#1a66c0" stroke-width="2"/>
    <use href="#badge-face"/>
  </svg>
</main>
</body>
</html>
```